R. Dunmore Homes, Inc business card (2 sided), letterhead (1 sided) & #10 envelope (1 sided)

business card of standard size utilizing the attached logo. Side one with logo, Carl Dunmore (my name), President / Broker (title), 805-555-0183 (phone), www.rdunmorehomes.example (website), 1275 Larkvale Avenue, Suite 4402 San Luis Obiso, CA 93499 (business address) carl.rdunmorehomes@mailbox.example (e-mail address),
Side two - Log

Letterhead and #10 envelope in the same theme

Reason: I think a 2 day deadline may be a bit ambitious on my part. I have extended the deadline to 4 days. Thanks!

```html
<!DOCTYPE html>
<html lang="en">
<head>
<meta charset="utf-8">
<title>R. Dunmore Homes, Inc – Stationery</title>
<link href="https://fonts.googleapis.com/css2?family=Open+Sans:wght@400;600&family=Roboto+Slab:wght@400;700&display=swap" rel="stylesheet">
<style>
  :root{
    --bg:#ece8e2;
    --paper:#ffffff;
    --blue:#1b6a90;
    --blue-dark:#0d4862;
    --blue-light:#2f8fbb;
    --ink:#2b2b2b;
    --faint:#d7e3ea;
    --rule:#3a3a3a;
  }
  *{box-sizing:border-box;margin:0;padding:0}
  html,body{width:1200px;height:718px;overflow:hidden;background:var(--bg)}
  body{position:relative;font-family:"Open Sans",Arial,sans-serif;color:var(--ink)}
  .sheet{position:absolute;background:var(--paper);box-shadow:0 1px 3px rgba(0,0,0,.25);overflow:hidden}
  .band{position:absolute;left:0;right:0;background:linear-gradient(90deg,var(--blue-dark),var(--blue-light) 50%,var(--blue-dark));color:#fff;white-space:nowrap}
  .band-rule{position:absolute;left:0;right:0;height:2px;background:var(--rule)}
  .brand{position:absolute;display:flex;align-items:center;gap:8px;font-family:"Roboto Slab",Georgia,serif;font-weight:700;color:var(--blue);white-space:nowrap}
  .brand .mark{width:12px;height:12px;background:var(--blue);flex:none}
  .brand.on-blue{color:#fff}
  .brand.on-blue .mark{background:#fff}
  .contact{list-style:none;font-size:8px;line-height:13px;white-space:nowrap}
  .contact li{display:flex;align-items:center;gap:4px}
  .icon{width:7px;height:7px;flex:none}

  /* Letterhead */
  .letterhead{left:27px;top:22px;width:479px;height:629px}
  .letterhead .brand{left:12px;top:40px;font-size:17px}
  .letterhead .contact{position:absolute;left:296px;top:18px;padding-left:7px;border-left:1px solid #bbb;font-size:7.5px}
  .letterhead .watermark{position:absolute;left:75px;top:318px;font-family:"Roboto Slab",Georgia,serif;font-weight:700;font-size:26px;color:var(--faint);white-space:nowrap}
  .letterhead .band-rule{top:590px}
  .letterhead .band{top:597px;height:32px;font-size:8.5px;text-align:center;line-height:18px}

  /* Envelopes */
  .env-back{left:617px;top:32px;width:539px;height:120px}
  .env-back .flap{position:absolute;left:0;top:0}
  .env-back .brand{left:190px;top:30px;font-size:14px}
  .env-mid{left:582px;top:138px;width:538px;height:110px;border:1px solid #888}
  .env-mid .flap{position:absolute;left:0;top:0}
  .env-mid .brand{left:192px;top:22px;font-size:14px}
  .env-front{left:542px;top:240px;width:538px;height:233px;border:1px solid #888}
  .env-front .brand{left:22px;top:38px;font-size:16px}
  .env-front address{position:absolute;left:32px;top:92px;font-style:normal;font-size:7.5px;line-height:14px}
  .env-front .band-rule{top:200px}
  .env-front .band{top:206px;height:27px;font-size:9.5px;letter-spacing:1.5px;line-height:23px;padding-left:22px}

  /* Business card */
  .card-front{left:542px;top:507px;width:311px;height:179px}
  .card-front .brand{left:10px;top:58px;font-size:10.5px;gap:6px}
  .card-front .brand .mark{width:10px;height:10px}
  .card-front .divider{position:absolute;left:168px;top:33px;width:1px;height:90px;background:#888}
  .card-front .who{position:absolute;left:175px;top:34px}
  .card-front .name{font-family:"Roboto Slab",Georgia,serif;font-weight:700;font-size:11px;color:var(--blue)}
  .card-front .title{font-family:"Roboto Slab",Georgia,serif;font-size:8.5px;margin:3px 0 6px}
  .card-front .contact{font-size:6.5px;line-height:12.5px}
  .card-front .badge{position:absolute;left:284px;top:124px;width:18px;height:30px;border:1px solid #222;background:#fff}
  .card-front .badge::before{content:"";position:absolute;left:2px;top:2px;width:12px;height:12px;background:#222}
  .card-front .band{top:161px;height:18px;font-size:7.5px;line-height:18px;padding-left:15px}
  .card-back{left:868px;top:505px;width:312px;height:177px;background:radial-gradient(ellipse at 50% 45%,var(--blue-light),var(--blue-dark) 85%)}
  .card-back .brand{left:58px;top:68px;font-size:17px}
  .card-back .site{position:absolute;left:0;right:0;top:146px;text-align:center;color:#fff;font-size:9.5px;letter-spacing:1.5px}
</style>
</head>
<body>

<svg width="0" height="0" style="position:absolute" aria-hidden="true">
  <symbol id="i-phone" viewBox="0 0 10 10"><circle cx="5" cy="5" r="5" fill="#1b6a90"/><path d="M3 2.5h1.3l.6 1.5-.8.6a4 4 0 0 0 1.5 1.5l.6-.8 1.5.6V7.5A5 5 0 0 1 3 2.5z" fill="#fff"/></symbol>
  <symbol id="i-mail" viewBox="0 0 10 10"><circle cx="5" cy="5" r="5" fill="#1b6a90"/><rect x="2.5" y="3.3" width="5" height="3.4" fill="#fff"/><path d="M2.5 3.3 5 5.3 7.5 3.3" fill="none" stroke="#1b6a90" stroke-width=".6"/></symbol>
  <symbol id="i-web" viewBox="0 0 10 10"><circle cx="5" cy="5" r="5" fill="#1b6a90"/><circle cx="5" cy="5" r="2.6" fill="none" stroke="#fff" stroke-width=".7"/><path d="M2.4 5h5.2M5 2.4v5.2" stroke="#fff" stroke-width=".6"/></symbol>
</svg>

<section class="sheet letterhead" aria-label="Letterhead">
  <div class="brand"><span class="mark"></span>R. Dunmore Homes, Inc</div>
  <ul class="contact">
    <li><svg class="icon"><use href="#i-phone"/></svg>805-555-0183</li>
    <li><svg class="icon"><use href="#i-mail"/></svg>carl.rdunmorehomes@mailbox.example</li>
    <li><svg class="icon"><use href="#i-web"/></svg>www.rdunmorehomes.example</li>
    <li>BRE License # 01948265</li>
  </ul>
  <div class="watermark" aria-hidden="true">R. Dunmore Homes, Inc</div>
  <div class="band-rule"></div>
  <div class="band">1275 Larkvale Avenue, Suite 4402, San Luis Obispo, CA 93499</div>
</section>

<section class="sheet env-back" aria-label="Envelope back">
  <svg class="flap" width="539" height="120" viewBox="0 0 539 120" aria-hidden="true">
    <defs><linearGradient id="flapGrad" x1="0" x2="1"><stop offset="0" stop-color="#0d4862"/><stop offset=".5" stop-color="#2f8fbb"/><stop offset="1" stop-color="#0d4862"/></linearGradient></defs>
    <path d="M0 0H539L519 105H20Z" fill="url(#flapGrad)"/>
  </svg>
  <div class="brand on-blue"><span class="mark"></span>R. Dunmore Homes, Inc</div>
</section>

<section class="sheet env-mid" aria-label="Envelope flap">
  <svg class="flap" width="538" height="110" viewBox="0 0 538 110" aria-hidden="true">
    <path d="M0 0 18 74H518L538 0" fill="none" stroke="#888" stroke-width="1"/>
  </svg>
  <div class="brand"><span class="mark"></span>R. Dunmore Homes, Inc</div>
</section>

<section class="sheet env-front" aria-label="#10 envelope front">
  <div class="brand"><span class="mark"></span>R. Dunmore Homes, Inc</div>
  <address>1275 Larkvale Avenue, Suite 4402<br>San Luis Obispo, CA 93499</address>
  <div class="band-rule"></div>
  <div class="band">www.rdunmorehomes.example</div>
</section>

<section class="sheet card-front" aria-label="Business card front">
  <div class="brand"><span class="mark"></span>R. Dunmore Homes, Inc</div>
  <div class="divider"></div>
  <div class="who">
    <p class="name">Carl Dunmore</p>
    <p class="title">President / Broker</p>
    <ul class="contact">
      <li><svg class="icon"><use href="#i-phone"/></svg>805-555-0183</li>
      <li><svg class="icon"><use href="#i-mail"/></svg>carl.rdunmorehomes@mailbox.example</li>
      <li><svg class="icon"><use href="#i-web"/></svg>www.rdunmorehomes.example</li>
      <li>BRE License # 01948265</li>
    </ul>
  </div>
  <div class="badge" aria-hidden="true"></div>
  <div class="band">1275 Larkvale Avenue, Suite 4402, San Luis Obispo, CA 93499</div>
</section>

<section class="sheet card-back" aria-label="Business card back">
  <div class="brand on-blue"><span class="mark"></span>R. Dunmore Homes, Inc</div>
  <p class="site">www.rdunmorehomes.example</p>
</section>

</body>
</html>
```